Business Card for my New Brokerage

Looking to get a business card design for my new Real Estate Brokerage.
I want it with Picture, Phone Number, Email, Website, Office Address
Name and Designation. Please add logo too.

Target Market(s)

Real Estate Investors or Home Buyers

Industry/Entity Type

Real Estate

Contact Information for Business Card

Name, Email, Phone Number, website, email, office address

Colors
EB3D1F
EC4F4E
F09395
F8D3D4
FCEDEE

Requirements
Must have
• Minimalistic, Clean, Modern, Photo
Nice to have
• White and Red Colors

```html
<!DOCTYPE html>
<html lang="en">
<head>
<meta charset="UTF-8">
<title>Lumen Realty Inc – Business Card</title>
<link rel="stylesheet" href="https://fonts.googleapis.com/css2?family=Montserrat:wght@600&family=Roboto:wght@400;500;700&display=swap">
<style>
  :root {
    --backdrop: #13304a;
    --brand-red: #e02a1e;
    --brand-red-deep: #c81d16;
    --accent-red: #d41f2b;
    --foil-gold: #d9c08a;
    --paper: #f6f5f3;
    --ink: #3c3c3c;
  }
  * { margin: 0; padding: 0; box-sizing: border-box; }
  html, body {
    width: 1200px; height: 1200px; overflow: hidden;
    background: var(--backdrop);
  }
  .stage { position: relative; width: 1200px; height: 1200px; }

  .card {
    position: absolute;
    left: 300px;
    width: 600px;
    height: 342px;
  }

  /* Front */
  .card-front {
    top: 220px;
    background: linear-gradient(135deg, #ef3a2a 0%, var(--brand-red) 45%, var(--brand-red-deep) 100%);
  }
  .front-wordmark {
    position: absolute;
    left: 0; right: 0; top: 140px;
    text-align: center;
    font-family: "Montserrat", sans-serif;
    font-weight: 600;
    color: var(--foil-gold);
    line-height: 1;
  }
  .front-wordmark .name { font-size: 72px; letter-spacing: 1px; display: block; }
  .front-wordmark .suffix { font-size: 23px; letter-spacing: 6px; display: block; margin-top: 12px; }

  /* Back */
  .card-back {
    top: 639px;
    background: var(--paper);
    font-family: "Roboto", sans-serif;
    color: var(--ink);
  }
  .back-wordmark {
    position: absolute;
    left: 40px; width: 240px; top: 150px;
    text-align: center;
    font-family: "Montserrat", sans-serif;
    font-weight: 600;
    color: var(--accent-red);
    line-height: 1;
  }
  .back-wordmark .name { font-size: 49px; display: block; }
  .back-wordmark .suffix { font-size: 16px; letter-spacing: 4px; display: block; margin-top: 6px; }

  .divider {
    position: absolute;
    left: 297px;
    width: 2px;
    background: var(--accent-red);
  }
  .divider-top { top: 85px; height: 41px; }
  .divider-bottom { top: 144px; height: 114px; }

  .identity { position: absolute; left: 324px; top: 83px; }
  .identity .person {
    font-size: 19px; font-weight: 700; color: var(--accent-red);
    line-height: 22px;
  }
  .identity .role { font-size: 17px; font-weight: 500; line-height: 22px; }

  .address {
    position: absolute; left: 324px; top: 144px;
    font-size: 16.5px; line-height: 22px; font-style: normal;
  }

  .contacts { position: absolute; left: 324px; top: 203px; list-style: none; }
  .contacts li {
    display: flex; align-items: center; gap: 7px;
    font-size: 16.5px; line-height: 23px;
  }
  .contacts svg { width: 16px; height: 16px; fill: var(--accent-red); flex: none; }
</style>
</head>
<body>
<main class="stage">
  <section class="card card-front" aria-label="Business card front">
    <div class="front-wordmark">
      <span class="name">LUMEN</span>
      <span class="suffix">REALTY INC</span>
    </div>
  </section>

  <section class="card card-back" aria-label="Business card back">
    <div class="back-wordmark">
      <span class="name">LUMEN</span>
      <span class="suffix">REALTY INC</span>
    </div>

    <span class="divider divider-top"></span>
    <span class="divider divider-bottom"></span>

    <div class="identity">
      <p class="person">MARCUS HOLLWAY</p>
      <p class="role">Managing Director</p>
    </div>

    <address class="address">
      48 Cedar Bend Road,<br>
      Maple Grove, ON L7K 3P2
    </address>

    <ul class="contacts">
      <li>
        <svg viewBox="0 0 24 24" aria-hidden="true"><path d="M6.6 10.8c1.4 2.8 3.8 5.1 6.6 6.6l2.2-2.2c.3-.3.7-.4 1-.2 1.1.4 2.3.6 3.6.6.6 0 1 .4 1 1V20c0 .6-.4 1-1 1C10.6 21 3 13.4 3 4c0-.6.4-1 1-1h3.5c.6 0 1 .4 1 1 0 1.3.2 2.5.6 3.6.1.3 0 .7-.2 1L6.6 10.8z"/></svg>
        (555) 214-7730
      </li>
      <li>
        <svg viewBox="0 0 24 24" aria-hidden="true"><path d="M2 5h20v14H2V5zm2 2v.5l8 5 8-5V7H4zm0 2.8V17h16V9.8l-8 5-8-5z"/></svg>
        hello@lumenrealty.com
      </li>
      <li>
        <svg viewBox="0 0 24 24" aria-hidden="true"><path d="M12 2a10 10 0 1 0 0 20 10 10 0 0 0 0-20zm0 2c1 0 2.3 1.9 2.8 5H9.2C9.7 5.9 11 4 12 4zM4.3 13a8 8 0 0 1 0-2h2.8a17 17 0 0 0 0 2H4.3zm.8 2h2.3c.3 1.3.7 2.4 1.2 3.3A8 8 0 0 1 5.1 15zm2.3-6H5.1a8 8 0 0 1 3.5-3.3C8.1 6.6 7.7 7.7 7.4 9zM12 20c-1 0-2.3-1.9-2.8-5h5.6c-.5 3.1-1.8 5-2.8 5zm3-7H9a15 15 0 0 1 0-2h6a15 15 0 0 1 0 2zm.4 5.3c.5-.9.9-2 1.2-3.3h2.3a8 8 0 0 1-3.5 3.3zM16.9 13a17 17 0 0 0 0-2h2.8a8 8 0 0 1 0 2h-2.8zm-.3-4c-.3-1.3-.7-2.4-1.2-3.3A8 8 0 0 1 18.9 9h-2.3z"/></svg>
        www.lumenrealty.com
      </li>
    </ul>
  </section>
</main>
</body>
</html>
```